Need a Modern WIX Website design

Need help designing a modern WIX website. I already started building on editor.wix.com but I am not a designer and would like a more modern, update aesthetic look. This is not an e-commerce site. Just a website portraying our company, posting what products we offer, contact, about us, services. Logo is already on the editor.wix version with some content. Need a designer with vision, and ingenuity to set it apart change it a little and make it stand out. Please look at the current site for redesign and/or ideas https://corvadetradewks.sitebuildr.net/website
also need the design to be connected to our google domain www.ctw.supply

Please feel free to ask as many questions as possible

Target Market(s)

Tire repair shops, Tire stores, mechanic shops, tire replacement franchises, wheel and rim stores

Industry/Entity Type

we are wholesalers, B2B ..sell tire repair materials, tire hand tools, machinery, chemicals, wheel lug nuts, wheel accessories

Coding

Coded - Design and coding required

Number of Pages Required

5+ page

Font styles to use
Other font styles liked:
• Let designer choose

Colors

Designer to choose colors to be used in the design.

Requirements
Must have
• modern design layout, videos, high quality pictures, different ideas for pages (Home, shop, about, products, services, contact, faq, meet the team) translatable english to spanish
Nice to have
• would like to have an up to date modern look, interactive, easy to navigate,
Should not have
• not be hard to navigate for our customers

```html
<!DOCTYPE html>
<html lang="en">
<head>
<meta charset="utf-8">
<title>Corvade Trade Works — Tire Repair Supplier in New York</title>
<link rel="stylesheet" href="https://fonts.googleapis.com/css2?family=Audiowide&family=Hind:wght@400;500;600;700&display=swap">
<style>
:root{
  --red:#e11f26;
  --red-dark:#b5161c;
  --ink:#1b1b1b;
  --black:#0e0e0e;
  --charcoal:#333333;
  --slate:#444444;
  --grey-bg:#ededed;
  --line:#bdbdbd;
  --text:#333;
  --white:#ffffff;
  --display:"Audiowide",sans-serif;
  --body:"Hind",sans-serif;
}
*{box-sizing:border-box;margin:0;padding:0}
html,body{width:1200px;height:5222px;overflow:hidden}
body{position:relative;font-family:var(--body);color:var(--text);background:var(--white)}
.abs{position:absolute}
.display{font-family:var(--display);text-transform:uppercase;letter-spacing:1px;color:var(--ink);font-weight:400}
.btn{position:absolute;background:var(--red);color:var(--white);font-family:var(--display);font-size:15px;display:flex;align-items:center;justify-content:center}
.photo{position:absolute}

/* top bar */
.topbar{top:0;left:0;width:1200px;height:73px;background:var(--black)}
.brand{position:absolute;display:flex;align-items:center;gap:10px;font-family:var(--body);font-weight:700;color:var(--white);font-size:24px;text-transform:uppercase;letter-spacing:1px}
.brand .mark{width:22px;height:22px;background:var(--red)}
.top-phone{left:762px;top:22px;color:var(--white);font-size:16px;display:flex;align-items:center;gap:10px;font-weight:500}
.socials{display:flex;gap:14px}
.socials span{width:12px;height:12px;border-radius:50%;background:var(--white);display:block}

/* nav */
.nav{top:73px;left:0;width:1200px;height:79px;background:var(--white);border-bottom:1px solid #e4e4e4}
.nav a{position:absolute;top:30px;font-size:18px;font-weight:500;color:var(--ink);text-decoration:none}
.nav a.current{color:var(--red);border:2px solid var(--red);padding:6px 8px 2px;top:22px}

/* hero */
.hero{top:152px;left:0;width:1200px;height:456px;background:var(--ink);overflow:hidden}
.hero .photo{left:0;top:0;width:1200px;height:456px;background:linear-gradient(100deg,#a8161c 0%,#c9262b 45%,#3a3a3a 75%,#202020 100%);clip-path:polygon(55% 0,100% 0,100% 100%,38% 100%,60% 50%)}
.hero .title-red{left:108px;top:110px;color:var(--red);font-size:37px}
.hero .title-white{left:108px;color:var(--white);font-size:64px;line-height:1}
.hero .arrow{top:208px;color:var(--white);font-size:30px}

/* about */
.about-heading{left:111px;top:682px;font-size:36px}
.about-sub{left:109px;top:742px;width:470px;font-family:var(--display);color:var(--red);font-size:22px;line-height:30px}
.about-copy{left:109px;top:812px;width:460px;font-size:15.5px;line-height:27px}
.frame-red{left:766px;top:661px;width:323px;height:450px;background:var(--red)}
.frame-white{left:645px;top:709px;width:391px;height:355px;background:var(--white);padding:6px;box-shadow:0 2px 8px rgba(0,0,0,.2)}
.frame-white .photo{position:relative;width:100%;height:100%;background:linear-gradient(135deg,#5d6670,#2b3036 60%,#9aa2aa)}

/* products */
.products{top:1188px;left:0;width:1200px;height:673px;background:var(--grey-bg)}
.product-box{left:111px;top:1275px;width:978px;height:501px;border:2px solid var(--ink);background:var(--white)}
.product-box .head{height:91px;border-bottom:2px solid var(--ink);position:relative}
.product-box .head h2{position:absolute;left:22px;top:24px;font-size:34px}
.cards{display:flex;height:406px}
.card{flex:1;border-right:2px solid var(--ink);display:flex;flex-direction:column}
.card:last-child{border-right:none}
.card .pic{height:280px;display:flex;align-items:center;justify-content:center}
.card .pic div{width:150px;height:70px;border-radius:10px;background:linear-gradient(180deg,#eaeaea,#8c8c8c 55%,#d0d0d0)}
.card .label{flex:1;background:var(--red);color:var(--white);text-align:center;padding-top:22px}
.card .label h3{font-size:22px;font-weight:500;line-height:26px}
.card .label p{font-size:15px;line-height:22px;padding:0 20px}

/* brands */
.brands{top:1861px;left:0;width:1200px;height:537px;background:#1c1c1c}
.brands h2{left:0;width:1200px;text-align:center;top:66px;color:var(--white);font-size:32px}
.brand-item{position:absolute;top:200px;width:220px;text-align:center;color:#e6e6e6;font-size:20px}
.brand-item .badge{width:134px;height:134px;margin:0 auto 42px;border:3px solid #bdbdbd;border-radius:50%}
.brand-item .badge.square{border-radius:6px;transform:rotate(45deg) scale(.8)}
.brands .arrow{top:246px;color:var(--white);font-size:34px}

/* values */
.values-band{top:2398px;left:0;width:1200px;height:792px;background:var(--slate)}
.values-bg{top:2434px;left:198px;width:1002px;height:795px;background:radial-gradient(circle at 70% 70%,#3b3f45,#15171a 70%)}
.values-red{left:85px;top:2459px;width:483px;height:730px;background:var(--red)}
.values-photo{left:116px;top:2489px;width:427px;height:679px;background:linear-gradient(160deg,#b8bcc2,#4a4e55 55%,#1d1f22)}
.value{position:absolute;width:240px;text-align:center;color:var(--white)}
.value .icon{width:70px;height:70px;border-radius:50%;background:var(--red);margin:0 auto 18px;display:flex;align-items:center;justify-content:center}
.value h3{font-size:18px;font-weight:600;margin-bottom:12px}
.value p{font-size:15px;line-height:24px;color:#ddd}

/* services */
.services-title{left:0;width:1200px;text-align:center;top:3342px;font-size:36px}
.svc-accent{left:109px;top:3456px;width:500px;height:294px;background:var(--red)}
.svc-photo-a{left:124px;top:3430px;width:476px;height:310px;background:linear-gradient(135deg,#2a2a2a,#111 60%,#b09020)}
.svc-caption{left:111px;top:3786px;font-size:19px;font-weight:700;color:var(--ink)}
.svc-copy{left:111px;top:3826px;width:420px;font-size:14.5px;line-height:22px;color:#555}
.svc-line{position:absolute;width:1px;height:38px;background:#555}
.svc-label{position:absolute;text-align:center;font-size:19px;font-weight:700;color:var(--ink);line-height:28px}
.svc-photo-b{left:612px;top:3661px;width:231px;height:227px;background:linear-gradient(160deg,#e0e3e6,#8d96a0 60%,#3b4048)}
.svc-photo-c{left:855px;top:3430px;width:234px;height:227px;background:linear-gradient(160deg,#c7c2b8,#6b6660 55%,#2d2b29)}

/* call banner */
.call{left:111px;top:3983px;width:980px;height:177px;background:var(--charcoal)}
.call h2{position:absolute;left:34px;top:60px;color:var(--white);font-size:35px;line-height:40px}
.call .num{position:absolute;left:672px;top:70px;display:flex;align-items:center;gap:10px;color:var(--white);font-size:31px;font-weight:600}
.call .num i{width:48px;height:48px;border-radius:50%;background:var(--red);display:flex;align-items:center;justify-content:center}

/* contact */
.contact-heading{left:180px;top:4300px;font-size:36px}
.contact-line{position:absolute;left:180px;display:flex;gap:22px;font-size:15px;color:#444;line-height:22px}
.contact-line svg{flex:none;margin-top:2px}
.field{position:absolute;border:1px solid #888;background:var(--white);font-size:15px;color:#555;padding:14px 16px}

/* footer */
.footer{top:4703px;left:0;width:1200px;height:519px;background:radial-gradient(circle at 50% 30%,#1f1f1f,#050505 75%)}
.footer .about-text{left:111px;top:4912px;width:320px;color:#ddd;font-size:15px;line-height:24px}
.footer h4{position:absolute;top:4812px;color:var(--white);font-size:21px;font-weight:500}
.footer .link{position:absolute;color:#ddd;font-size:15px}
.footer .mail{left:823px;top:4871px;width:266px;height:39px;border:1px solid #ccc;color:#ddd;font-size:13px;padding:11px 26px}
.footer .copy{left:0;width:1200px;top:5152px;text-align:center;color:var(--white);font-size:15px}
.footer .copy span{color:var(--red)}
</style>
</head>
<body>

<!-- top bar -->
<header class="topbar abs">
  <div class="brand" style="left:108px;top:22px"><span class="mark"></span>Corvade Trade Works</div>
  <div class="top-phone abs">
    <svg width="16" height="16" viewBox="0 0 24 24"><path fill="#e11f26" d="M6.6 10.8a15 15 0 0 0 6.6 6.6l2.2-2.2c.3-.3.7-.4 1-.2 1.1.4 2.3.6 3.6.6.6 0 1 .4 1 1V20c0 .6-.4 1-1 1A17 17 0 0 1 3 4c0-.6.4-1 1-1h3.5c.6 0 1 .4 1 1 0 1.3.2 2.5.6 3.6.1.3 0 .7-.2 1z"/></svg>
    833-555-0147
  </div>
  <div class="socials abs" style="left:1018px;top:30px"><span></span><span></span><span></span></div>
</header>

<!-- nav -->
<nav class="nav abs">
  <a class="current" style="left:107px">Home</a>
  <a style="left:189px">Shop</a>
  <a style="left:264px">About</a>
  <a style="left:349px">Products</a>
  <a style="left:458px">Services</a>
  <a style="left:562px">Contact</a>
  <a style="left:661px">FAQ</a>
  <a style="left:730px">Meet the Team</a>
  <a style="left:888px">Wheel Lug Nuts &amp; Bolts</a>
</nav>

<!-- hero -->
<section class="hero abs">
  <div class="photo" role="img" aria-label="Smiling mechanic rolling a tire in a workshop, tinted red"></div>
  <div class="display title-red abs">Tire Repair</div>
  <div class="display title-white abs" style="top:152px">Supplier</div>
  <div class="display title-white abs" style="top:222px;font-size:52px">In New York</div>
  <div class="btn" style="left:109px;top:301px;width:132px;height:40px">Contact Us</div>
  <div class="arrow abs" style="left:62px">&#8249;</div>
  <div class="arrow abs" style="left:1112px">&#8250;</div>
</section>

<!-- about -->
<h2 class="display about-heading abs">About Us</h2>
<p class="about-sub abs">Your One Stop Tire Repair Supplier in New York</p>
<div class="about-copy abs">
  <p>At Corvade Trade Works we make sure to offer our clients the best selection of tire repair products, tools and machinery as well as provide them with superb customer service.</p>
  <p>Our staff works with our customers to find exactly the right part they need for the right price. We're here to help inform you about our products, so that you only buy what is absolutely necessary for your establishment. Contact us today to learn more about what we do.</p>
</div>
<div class="btn" style="left:109px;top:1074px;width:132px;height:39px">Read More</div>
<div class="frame-red abs"></div>
<div class="frame-white abs"><div class="photo" role="img" aria-label="Mechanic kneeling beside a car changing a wheel"></div></div>

<!-- products -->
<section class="products abs"></section>
<div class="product-box abs">
  <div class="head">
    <h2 class="display">Our Products</h2>
    <div class="btn" style="left:827px;top:24px;width:130px;height:40px">View All</div>
  </div>
  <div class="cards">
    <div class="card"><div class="pic"><div role="img" aria-label="Chrome lug nut" style="width:110px;height:110px"></div></div><div class="label"><h3>Lug</h3><p>Trucks/SUVs/Vans (7/8) M14 1.5</p></div></div>
    <div class="card"><div class="pic"><div role="img" aria-label="Spline lug nut adapter" style="width:200px;height:40px"></div></div><div class="label"><h3>Spline Lug Nut</h3><p>Adapter - Truck Spline w/</p></div></div>
    <div class="card"><div class="pic"><div role="img" aria-label="Long spline drive adapter" style="width:210px;height:34px"></div></div><div class="label"><h3>Kenzaru</h3><p>Adapter - Car Spline w/ 3/4 and 13/16 Drives</p></div></div>
    <div class="card"><div class="pic"><div role="img" aria-label="Six sided spline lug nut" style="width:120px;height:130px"></div></div><div class="label"><h3>Spline Lug Nut</h3><p>Car (6 Sided)</p></div></div>
  </div>
</div>

<!-- brands -->
<section class="brands abs">
  <h2 class="display abs">Brands</h2>
  <div class="arrow abs" style="left:86px">&#8249;</div>
  <div class="brand-item" style="left:155px"><div class="badge square"></div>Halvor Tip Co</div>
  <div class="brand-item" style="left:374px"><div class="badge"></div>Keystrand Inc</div>
  <div class="brand-item" style="left:601px"><div class="badge square"></div>Brackwell Industries</div>
  <div class="brand-item" style="left:828px"><div class="badge"></div>Tamsin Row Industries</div>
  <div class="arrow abs" style="left:1088px">&#8250;</div>
</section>

<!-- values -->
<div class="values-band abs"></div>
<div class="values-bg abs" role="img" aria-label="Dark close-up of tire treads"></div>
<div class="values-red abs"></div>
<div class="values-photo abs" role="img" aria-label="Worker carrying a new tire"></div>
<div class="value" style="left:591px;top:2566px">
  <div class="icon"><svg width="34" height="34" viewBox="0 0 24 24" fill="none" stroke="#fff" stroke-width="1.6"><path d="M3 12l4-4 5 3 5-3 4 4-9 7z"/></svg></div>
  <h3>Commitment</h3><p>We understand, respect and value our customers, taking an interest and the time to listen.</p>
</div>
<div class="value" style="left:859px;top:2566px">
  <div class="icon"><svg width="34" height="34" viewBox="0 0 24 24" fill="none" stroke="#fff" stroke-width="1.6"><circle cx="12" cy="10" r="6"/><path d="M9 19h6M10 22h4"/></svg></div>
  <h3>Innovation</h3><p>We keep innovating to improve the experience for customers and everyone who uses our spaces.</p>
</div>
<div class="value" style="left:591px;top:2876px">
  <div class="icon"><svg width="34" height="34" viewBox="0 0 24 24" fill="none" stroke="#fff" stroke-width="1.6"><circle cx="12" cy="12" r="4"/><path d="M12 2v4M12 18v4M2 12h4M18 12h4M5 5l3 3M16 16l3 3M19 5l-3 3M8 16l-3 3"/></svg></div>
  <h3>Simplicity</h3><p>We get things done simply and flexibly.<br>We remove unnecessary obstacles so that we are easy for our customers to deal with.</p>
</div>
<div class="value" style="left:859px;top:2876px">
  <div class="icon"><svg width="34" height="34" viewBox="0 0 24 24" fill="none" stroke="#fff" stroke-width="1.6"><path d="M4 14h4l4 4 8-8M12 4v7M9 8l3 3 3-3"/></svg></div>
  <h3>Excellence</h3><p>We achieve high quality in everything we do, committing to excellence in how we do business.<br>Highly professional, we offer exemplary customer service.</p>
</div>

<!-- services -->
<h2 class="display services-title abs">Services Offered</h2>
<div class="svc-accent abs"></div>
<div class="svc-photo-a photo" role="img" aria-label="Gloved hand using an impact wrench on a wheel"></div>
<div class="svc-line" style="left:124px;top:3740px;height:30px"></div>
<div class="svc-caption abs">High Quality Products</div>
<p class="svc-copy abs">Our products are trusted for their design &amp; engineering, &amp; we will continue to equip our customers with high-quality products and tools at the best value</p>
<div class="svc-label" style="left:612px;top:3548px;width:231px">Stellar Customer<br>Service</div>
<div class="svc-line" style="left:728px;top:3610px"></div>
<div class="svc-photo-b photo" role="img" aria-label="Mechanic holding wrenches"></div>
<div class="svc-photo-c photo" role="img" aria-label="Two men shaking hands in a tire showroom"></div>
<div class="svc-line" style="left:972px;top:3666px"></div>
<div class="svc-label" style="left:855px;top:3722px;width:234px">Commitment</div>

<!-- call banner -->
<section class="call abs">
  <h2 class="display" style="color:#fff">Call Now For A<br>Free Consultation</h2>
  <div class="num"><i><svg width="24" height="24" viewBox="0 0 24 24"><path fill="#fff" d="M6.6 10.8a15 15 0 0 0 6.6 6.6l2.2-2.2c.3-.3.7-.4 1-.2 1.1.4 2.3.6 3.6.6.6 0 1 .4 1 1V20c0 .6-.4 1-1 1A17 17 0 0 1 3 4c0-.6.4-1 1-1h3.5c.6 0 1 .4 1 1 0 1.3.2 2.5.6 3.6.1.3 0 .7-.2 1z"/></svg></i>833-555-0147</div>
</section>

<!-- contact -->
<h2 class="display contact-heading abs">Contact Us</h2>
<div class="contact-line" style="top:4384px;color:var(--red)">
  <svg width="16" height="22" viewBox="0 0 16 22"><path fill="#e11f26" d="M8 0a8 8 0 0 0-8 8c0 6 8 14 8 14s8-8 8-14a8 8 0 0 0-8-8zm0 11a3 3 0 1 1 0-6 3 3 0 0 1 0 6z"/></svg>
  <span>48 Harlow Mill Road, Ridgefield<br>NY 11790 Suite 4</span>
</div>
<div class="contact-line" style="top:4466px">
  <svg width="18" height="14" viewBox="0 0 18 14"><path fill="#222" d="M0 0h18v14H0zm2 2v1l7 5 7-5V2L9 7z"/></svg>
  <span>customerservice@ctw.supply</span>
</div>
<div class="contact-line" style="top:4528px">
  <svg width="18" height="18" viewBox="0 0 24 24"><path fill="#222" d="M6.6 10.8a15 15 0 0 0 6.6 6.6l2.2-2.2c.3-.3.7-.4 1-.2 1.1.4 2.3.6 3.6.6.6 0 1 .4 1 1V20c0 .6-.4 1-1 1A17 17 0 0 1 3 4c0-.6.4-1 1-1h3.5c.6 0 1 .4 1 1 0 1.3.2 2.5.6 3.6.1.3 0 .7-.2 1z"/></svg>
  <span>833-555-0147</span>
</div>
<div class="field" style="left:565px;top:4245px;width:463px;height:51px">Name</div>
<div class="field" style="left:565px;top:4306px;width:463px;height:51px">Address</div>
<div class="field" style="left:565px;top:4368px;width:225px;height:51px">Email</div>
<div class="field" style="left:803px;top:4368px;width:225px;height:51px">Phone</div>
<div class="field" style="left:565px;top:4431px;width:463px;height:51px">Subject</div>
<div class="field" style="left:565px;top:4494px;width:463px;height:122px">Type your message here . . .</div>
<div class="btn" style="left:898px;top:4624px;width:130px;height:38px">Submit Now</div>

<!-- footer -->
<footer class="footer abs"></footer>
<div class="brand" style="left:111px;top:4822px;font-size:22px"><span class="mark"></span>Corvade Trade Works</div>
<p class="about-text abs" style="left:111px;top:4912px;width:320px;color:#ddd;font-size:15px;line-height:24px">Corvade Trade Works, Inc has been serving our customers for more than 25 years! While the company was founded as Corvade Supply Corp in 1996, its roots can be traced back to 1985 .</p>
<h4 style="position:absolute;left:493px;top:4812px;color:#fff;font-size:21px;font-weight:500">Quick Link</h4>
<div class="link" style="position:absolute;left:494px;top:4876px;color:#ddd;font-size:15px">Home</div>
<div class="link" style="position:absolute;left:494px;top:4914px;color:#ddd;font-size:15px">Shop</div>
<div class="link" style="position:absolute;left:494px;top:4951px;color:#ddd;font-size:15px">About</div>
<div class="link" style="position:absolute;left:494px;top:4989px;color:#ddd;font-size:15px">Products</div>
<div class="link" style="position:absolute;left:494px;top:5026px;color:#ddd;font-size:15px">Services</div>
<div class="link" style="position:absolute;left:610px;top:4876px;color:#ddd;font-size:15px">Contact</div>
<div class="link" style="position:absolute;left:610px;top:4914px;color:#ddd;font-size:15px">FAQ</div>
<div class="link" style="position:absolute;left:610px;top:4951px;color:#ddd;font-size:15px">Meet the Team</div>
<div class="link" style="position:absolute;left:610px;top:4989px;color:#ddd;font-size:15px">Wheel Lug Nuts &amp; Bolts</div>
<h4 style="position:absolute;left:823px;top:4812px;color:#fff;font-size:21px;font-weight:500">Get our news and updates</h4>
<div style="position:absolute;left:823px;top:4871px;width:266px;height:39px;border:1px solid #ccc;color:#ddd;font-size:13px;padding:11px 26px">Enter Your Mail Here</div>
<div class="btn" style="left:823px;top:4922px;width:132px;height:39px">Subscribe</div>
<div class="socials abs" style="left:828px;top:5030px"><span></span><span></span><span></span></div>
<div style="position:absolute;left:0;width:1200px;top:5152px;text-align:center;color:#fff;font-size:15px">©2035 by <span style="color:var(--red)">CORVADETRADEWORKS</span>. All Right Reserved</div>

</body>
</html>
```